Mossy Den Pet Supply

Thank you for your interest in this design contest. We are always welcome to questions and are looking forward to seeing what you can come up with.

We work on a Bootstrap platform with our custom built CMS. We require all designs to be sized accordingly with the bootstrap grid system found here: http://fernlattice.com/css/#grid

At the start of a competition, we are looking for general Home Page Design concepts and an example product grid page.

Homepage: Slide Show/Featured Products/Specials

example website as a reference:https://www.mintcollarworks.com/

Store Product Grid: Show a grid of product thumbnails. Included elements are thumbnail and price. Also included are filters (sort by, show by grid/list).

No photos at this time but Logo is attached. Looking for good quality photo's around the web. Please read the attached creative brief in depth to get an idea f what the client is looking for. Thanks!

```html
<!DOCTYPE html>
<html lang="en">
<head>
<meta charset="utf-8">
<title>Mossy Den Pet Supply</title>
<link href="https://fonts.googleapis.com/css2?family=Arimo:wght@400;700&family=Ubuntu:wght@400;500;700&family=Pinyon+Script&display=swap" rel="stylesheet">
<style>
:root{
  --green:#8cc21f;
  --green-dark:#6fa010;
  --blue:#1a9ad6;
  --page-bg:#ececec;
  --panel:#ffffff;
  --band:#e6e6e6;
  --text:#3f3f3f;
  --muted:#8a8a8a;
  --accent-red:#e0400e;
  --quote:#777;
}
*{margin:0;padding:0;box-sizing:border-box}
html,body{width:858px;height:1200px;overflow:hidden}
body{position:relative;background:var(--page-bg);font-family:Arimo,Arial,sans-serif;color:var(--text)}
.abs{position:absolute}
.hero{left:0;top:0;width:858px;height:356px;
  background:
    radial-gradient(ellipse 120px 110px at 300px 250px,rgba(232,178,28,.95),rgba(232,178,28,0) 100%),
    radial-gradient(ellipse 70px 60px at 385px 285px,rgba(250,244,232,.95),rgba(250,244,232,0) 100%),
    radial-gradient(ellipse 60px 55px at 180px 300px,rgba(176,128,82,.85),rgba(176,128,82,0) 100%),
    radial-gradient(ellipse 140px 150px at 650px 220px,rgba(118,124,104,.95),rgba(118,124,104,0) 100%),
    radial-gradient(ellipse 45px 50px at 600px 200px,rgba(120,84,52,.8),rgba(120,84,52,0) 100%),
    radial-gradient(ellipse 200px 70px at 480px 120px,rgba(232,234,236,.85),rgba(232,234,236,0) 100%),
    linear-gradient(90deg,rgba(70,72,52,.55) 0%,rgba(70,72,52,0) 22%,rgba(70,72,52,0) 80%,rgba(90,92,72,.45) 100%),
    linear-gradient(180deg,#c6cdc0 0%,#9aa48c 30%,#8c9468 52%,#93a84e 70%,#a9bc5e 100%);}
.navbar{left:0;top:0;width:858px;height:42px;background:linear-gradient(#4a4a4a,#262626);border-bottom:1px solid #111}
.nav{position:absolute;left:230px;top:0;display:flex;height:42px;font-family:Ubuntu,sans-serif;font-size:9px;color:#fff}
.nav a{display:flex;align-items:center;padding:0 13px;border-left:1px solid #1c1c1c;box-shadow:inset 1px 0 0 #555;color:#fff;text-decoration:none;white-space:nowrap}
.nav a.active{background:#0c0c0c;padding:0 22px;box-shadow:none;position:relative}
.nav a.active::after{content:"";position:absolute;left:50%;bottom:0;width:32px;height:8px;margin-left:-16px;background:var(--green);border-radius:16px 16px 0 0}
.brand{left:73px;top:0;width:99px;height:86px;background:#fff;border-radius:0 0 8px 8px;box-shadow:0 1px 4px rgba(0,0,0,.4);display:flex;align-items:center;justify-content:center;text-align:center;font-family:Ubuntu,sans-serif;font-weight:700;font-size:12px;line-height:14px;color:var(--green-dark);padding:0 6px}
.panel{left:73px;top:337px;width:712px;height:775px;background:var(--panel)}
.card{top:352px;width:217px;height:133px;background:linear-gradient(#fff,#f1f1f1);border:1px solid #d6d6d6;border-radius:4px;overflow:hidden}
.pill{position:absolute;left:7px;top:17px;width:154px;height:24px;background:linear-gradient(#9fd232,var(--green));border-radius:12px;color:#fff;font-family:Ubuntu,sans-serif;font-size:13px;line-height:24px;padding-left:16px;letter-spacing:.3px}
.ribbon{position:absolute;right:0;top:0}
.card .ph{position:absolute}
.card h3{position:absolute;left:24px;top:46px;font-size:13.5px;font-weight:400;color:#222;letter-spacing:-.3px;z-index:2}
.tips{position:absolute;left:22px;top:68px;list-style:none;font-size:8px;line-height:13px;color:var(--accent-red);z-index:2}
.tips li::before{content:"";display:inline-block;border-left:4px solid var(--accent-red);border-top:3px solid transparent;border-bottom:3px solid transparent;margin-right:6px}
.card h4{position:absolute;left:23px;top:46px;font-size:14px;font-weight:700;color:#333;letter-spacing:1px;line-height:17px;z-index:2}
.card p{position:absolute;left:23px;font-size:8.5px;line-height:12px;color:#777;z-index:2}
.card .big{position:absolute;left:21px;top:46px;font-size:18px;font-weight:700;color:#2a2a2a;letter-spacing:-.4px;z-index:2}
.guide{left:73px;top:508px;width:712px;text-align:center}
.guide h1{font-size:27px;font-weight:400;color:#444;letter-spacing:1.5px}
.guide h2{font-size:16px;font-weight:400;color:var(--muted);letter-spacing:.6px;margin-top:2px}
.guide p{font-size:10.5px;line-height:17px;color:#555;margin:17px 10px 0}
.btn{left:388px;top:646px;width:68px;height:31px;border-radius:4px;background:linear-gradient(#9fd83a,#7bb515);border:1px solid #b6e070;box-shadow:0 0 0 1px #8cc21f;color:#fff;font-size:10.5px;line-height:29px;text-align:center}
.rule{left:81px;width:690px;height:5px;background:radial-gradient(ellipse at center,rgba(0,0,0,.12) 0%,rgba(0,0,0,0) 70%)}
.video{left:89px;top:723px;width:283px;height:187px;background:#a8a8a8;border-radius:4px;padding:7px;box-shadow:0 8px 10px -6px rgba(0,0,0,.35)}
.video .ph{width:100%;height:100%;border:2px solid #fff;background:linear-gradient(120deg,#efe2cc 0%,#d8b897 40%,#b7b7c4 70%,#e8e8ef 100%);position:relative}
.video svg{position:absolute;left:50%;top:50%;margin:-20px 0 0 -20px}
.pubs{left:406px;top:712px;width:366px}
.pubs h2{font-family:Ubuntu,sans-serif;font-weight:400;font-size:22px;color:var(--green);margin-bottom:6px}
.pubs p{font-size:8.3px;line-height:13px;color:#222;margin-bottom:13px;text-align:justify}
.quote{left:410px;top:856px;width:360px;height:56px}
.quote .mark{position:absolute;left:0;top:0;font-family:Georgia,serif;font-size:34px;font-weight:700;color:#c92616;line-height:34px}
.quote .line{position:absolute;font-family:"Pinyon Script",cursive;font-size:18px;color:var(--quote);white-space:nowrap}
.band{left:73px;top:959px;width:712px;height:117px;background:var(--band)}
.thumb{top:972px;width:106px;height:92px;background:#fff;border:1px solid #d4d4d4;padding:3px}
.thumb div{width:100%;height:100%}
.teaser{top:974px;width:92px;font-size:8.8px;line-height:13px;color:#555}
.teaser h5{font-size:9.5px;font-weight:700;color:var(--green);margin-bottom:6px}
.teaser b{display:block;margin-top:3px;color:#444;font-size:9px}
.footer{left:0;top:1106px;width:858px;height:94px;background:linear-gradient(180deg,rgba(140,194,31,0) 0%,var(--green) 12%,var(--green) 100%)}
.footer-scene{left:0;top:1100px;width:858px;height:36px}
.copyright{left:0;top:1173px;width:858px;text-align:center;font-size:8.5px;color:#fff}
</style>
</head>
<body>

<div class="abs hero" role="img" aria-label="Photo of a smiling woman in a yellow top and a man in uniform crouching on a lawn before a white house, with a shar-pei, a pomeranian and a yorkshire terrier"></div>

<header>
  <div class="abs navbar"></div>
  <nav class="nav">
    <a class="active">Home</a><a>About Pal</a><a>Pet Facts</a><a>Poetry Contest</a><a>Pet Links</a><a>Featured Products</a><a>Our Video</a><a>Pal Blog</a>
  </nav>
  <div class="abs brand">Mossy Den Pet Supply</div>
</header>

<main>
  <div class="abs panel"></div>

  <section class="abs card" style="left:83px">
    <div class="pill">Intoduction</div>
    <svg class="ribbon" width="60" height="60" viewBox="0 0 60 60"><polygon points="14,0 34,0 60,26 60,46" fill="var(--green)"/><text x="0" y="0" transform="translate(40,22) rotate(45)" fill="#fff" font-family="Arimo,sans-serif" font-size="9" font-weight="700" text-anchor="middle">ADVICE</text></svg>
    <div class="ph" role="img" aria-label="Photo of two women with a golden retriever and a terrier" style="left:120px;top:62px;width:97px;height:71px;background:linear-gradient(90deg,rgba(241,241,241,0),#d8c0a0 25%,#9a7656 60%,#c89a74)"></div>
    <h3>Tips from the top</h3>
    <ul class="tips"><li>Grooming</li><li>Training</li><li>Care</li><li>Puppy &amp; Kitten</li></ul>
  </section>

  <section class="abs card" style="left:318px">
    <div class="pill">Pet Facts</div>
    <svg class="ribbon" width="60" height="60" viewBox="0 0 60 60"><polygon points="14,0 34,0 60,26 60,46" fill="var(--blue)"/><text x="0" y="0" transform="translate(40,22) rotate(45)" fill="#fff" font-family="Arimo,sans-serif" font-size="11" font-weight="700" text-anchor="middle">NEW</text></svg>
    <div class="ph" role="img" aria-label="Photo of a sitting shar-pei puppy" style="left:140px;top:56px;width:70px;height:74px;background:radial-gradient(ellipse at 55% 50%,#c8925e 0%,#d9ad7f 40%,rgba(241,241,241,0) 70%)"></div>
    <h4>Comet Pup's<br>Orbit</h4>
    <p style="top:88px">Give your pet the salon style<br>with the Glenmoor Pro Slicker</p>
  </section>

  <section class="abs card" style="left:554px">
    <div class="pill">Poetry Contest</div>
    <svg class="ribbon" width="60" height="60" viewBox="0 0 60 60"><polygon points="14,0 34,0 60,26 60,46" fill="var(--green)"/><text x="0" y="0" transform="translate(40,22) rotate(45)" fill="#fff" font-family="Arimo,sans-serif" font-size="9" font-weight="700" text-anchor="middle">PUPPY</text></svg>
    <div class="ph" role="img" aria-label="Photo of a small jack russell terrier puppy" style="left:168px;top:66px;width:36px;height:66px;background:radial-gradient(ellipse at 50% 50%,#e9e3da 0%,#cdbfae 50%,rgba(241,241,241,0) 75%)"></div>
    <div class="big">Start them young</div>
    <p style="top:70px;left:21px">Make training your pup a cleaner<br>and easier process with the<br>PuppyStride range</p>
  </section>

  <section class="abs guide">
    <h1>WELLBEING GUIDE</h1>
    <h2>FOR YOUR All Pets</h2>
    <p>Lorem Ipsum is simply dummy text of the printing and typesetting industry. Lorem Ipsum has been the industry's standard dummy text ever since the 1500s, when an unknown printer took a galley of type and scrambled it to make a type specimen book. It has survived not only five centuries, but also the leap into electronic typesetting.....</p>
  </section>
  <div class="abs btn">More info</div>

  <div class="abs rule" style="top:690px"></div>

  <div class="abs video">
    <div class="ph" role="img" aria-label="Photo of a girl lying beside a laughing dog, holding a remote control">
      <svg width="40" height="40" viewBox="0 0 40 40"><circle cx="20" cy="20" r="18" fill="#fff" stroke="#9a9a9a" stroke-width="2"/><circle cx="20" cy="20" r="13" fill="#2a2a2a"/><polygon points="16,13 16,27 27,20" fill="#fff"/></svg>
    </div>
  </div>

  <section class="abs pubs">
    <h2>Popular Publications</h2>
    <p>Lorem Ipsum is simply dummy text of the printing and typesetting industry. Lorem Ipsum has been the industry's standard dummy text ever since the 1500s, when an unknown printer took a galley of type and scrambled it to make a type specimen book. It has survived not only five centuries, but also the leap into electronic typesetting,</p>
    <p>It was popularised in the 1960s with the release of Typeline sheets containing Lorem Ipsum passages, and more recently with desktop publishing software like Quillset PageComposer including versions of Lorem Ipsum.</p>
  </section>

  <blockquote class="abs quote">
    <span class="mark">&#8220;</span>
    <span class="line" style="left:30px;top:10px">Your promotional text here Vivamus</span>
    <span class="line" style="left:90px;top:30px">volutpat ante, sit amet semper nisi</span>
  </blockquote>

  <div class="abs rule" style="top:937px"></div>

  <section class="abs band"></section>
  <div class="abs thumb" style="left:88px"><div role="img" aria-label="Photo of a fluffy puppy in a field of wildflowers" style="background:linear-gradient(160deg,#6c6a3a,#c0a06a 55%,#8a7a3a)"></div></div>
  <div class="abs teaser" style="left:207px"><h5>Ipsum is simply</h5>text of the printype-setting indu Lorem Ipsum has been the industry's standard<b>More...</b></div>
  <div class="abs thumb" style="left:319px"><div role="img" aria-label="Photo of a puppy and a kitten on a wooden chair" style="background:linear-gradient(160deg,#c85a20,#e8c9a0 50%,#7aaed0)"></div></div>
  <div class="abs teaser" style="left:438px"><h5>Ipsum is simply</h5>text of the printype-setting indu Lorem Ipsum has been the industry's standard<b>More...</b></div>
  <div class="abs thumb" style="left:553px"><div role="img" aria-label="Photo of a bloodhound and a kitten sleeping together" style="background:linear-gradient(160deg,#3a1c10,#9a5228 50%,#5a2e18)"></div></div>
  <div class="abs teaser" style="left:672px"><h5>Ipsum is simply</h5>text of the printype-setting indu Lorem Ipsum has been the industry's standard<b>More...</b></div>
</main>

<footer>
  <div class="abs footer"></div>
  <div class="abs footer-scene" role="img" aria-label="Green silhouette strip of dog houses, trees and people walking dogs" style="background:linear-gradient(180deg,rgba(140,194,31,0),rgba(140,194,31,.6))"></div>
  <p class="abs copyright">&copy; Copyright 2013 Mossy Den Pet Supply (NPSA)</p>
</footer>

</body>
</html>
```